New Business Card Design for Manufacturing

We are an engineering/manufacturing company that offers Advanced machining/assembly/engineering services, as well as innovative products for the heavy duty engine cooling markets.

We are looking to get a new business card designed that is clean and modern looking, but still fits the wide range of technical/skilled work we do.

- We hope to use this design as the base for other design work in new Presentations, web, and print work.

Industry/Entity Type

Engineering

Contact Information for Business Card

Our preferred color of blue is (RGB) 22/71/159 but can vary slightly from that color. Our content will be our Logo and full company name (Fabricated Tooling Works, Inc.), company address, name, job title, phone number with extension, cell number, fax number, website, and email address on the cards.
We'd like the full company name next to the logo, but we are open to other interpretations of that layout.
Preferably, we would like the back side to be clean with just our logo, and the front to contain all of the contact information.

Colors
2f74b4
0355a3
85abd2

Requirements
Must have
• - Logo, company name, needed content - We are open to interpretation beyond that.
• - Standard size business card.
• - Horizontal orientation.
• - Enough space for lengthy names / job titles (for example, a job title could read "Directory of Human Resources" or "V.P. of Governmental Affairs"). We need this to look clean, whether the title be short (CEO) or long (as described above).

```html
<!DOCTYPE html>
<html lang="en">
<head>
<meta charset="utf-8">
<title>Fabricated Tooling Works – Business Card</title>
<link rel="stylesheet" href="https://fonts.googleapis.com/css2?family=Arimo:wght@400;700&display=swap">
<style>
  :root {
    --backdrop: #191919;
    --card-light: #e8e8e8;
    --card-blue: #0d52a0;
    --brand-blue: #0f4ea3;
    --brand-grey: #8a8d90;
    --ink-white: #ffffff;
    --rule: rgba(255, 255, 255, 0.45);
  }
  * { margin: 0; padding: 0; box-sizing: border-box; }
  html, body {
    width: 1200px; height: 900px; overflow: hidden;
    background: var(--backdrop);
    font-family: "Arimo", Arial, sans-serif;
  }
  .canvas { position: relative; width: 1200px; height: 900px; }

  /* Standard 3.5 x 2 in horizontal cards */
  .card {
    position: absolute; top: 291px;
    width: 460px; height: 263px; border-radius: 6px;
    box-shadow: 0 3px 8px rgba(0, 0, 0, 0.45);
  }
  .card--back { left: 90px; background: var(--card-light); }
  .card--front { left: 650px; background: var(--card-blue); color: var(--ink-white); }

  /* Back side: brand lockup and web address */
  .brand {
    position: absolute; left: 0; width: 460px; top: 76px;
    display: flex; align-items: center; justify-content: center; gap: 16px;
  }
  .brand-mark {
    width: 52px; height: 52px; flex: none;
    background: var(--brand-blue);
  }
  .company-name {
    font-weight: 700; font-size: 24px; line-height: 28px;
    color: var(--brand-blue); letter-spacing: 0.4px;
  }
  .web-address {
    position: absolute; left: 0; width: 460px; top: 182px;
    text-align: center;
    font-weight: 700; font-size: 14px; letter-spacing: 1.5px;
    color: var(--brand-blue);
  }
  .web-address .domain { color: var(--brand-grey); }

  /* Front side: contact details */
  .contact {
    position: absolute; left: 0; width: 460px; top: 28px;
    text-align: center;
  }
  .person-name { font-weight: 700; font-size: 22px; line-height: 26px; }
  .job-title { font-size: 16px; line-height: 20px; }
  .divider {
    width: 172px; height: 1px; margin: 9px auto;
    background: var(--rule);
  }
  .contact-lines { list-style: none; font-size: 16px; line-height: 20px; }
  .contact-lines b { font-weight: 700; }
  .postal { font-style: normal; font-size: 16px; line-height: 20px; }
</style>
</head>
<body>
<main class="canvas">
  <section class="card card--back" aria-label="Card back">
    <div class="brand">
      <span class="brand-mark" aria-hidden="true"></span>
      <p class="company-name">FABRICATED TOOLING<br>WORKS, INC.</p>
    </div>
    <p class="web-address">WWW.<span class="domain">FABTOOLINGWORKS</span>.COM</p>
  </section>

  <section class="card card--front" aria-label="Card front">
    <div class="contact">
      <p class="person-name">DANIEL HARTLEY</p>
      <p class="job-title">Managing Director</p>
      <div class="divider"></div>
      <ul class="contact-lines">
        <li><b>P:</b> (044)987654321</li>
        <li><b>M:</b> (044)987654321</li>
        <li><b>F:</b> (044)987654321</li>
        <li><b>E:</b> info@fabtoolingworks.com</li>
      </ul>
      <div class="divider"></div>
      <address class="postal">5820, Foundry Lane,<br>Springfield, 45502</address>
    </div>
  </section>
</main>
</body>
</html>
```